Wallaby and Rabbit deterrent flyer

I am after a one page flyer for the advertisement of a rabbit and wallaby deterrent. I am doing some targeted advertising of a product that deters rabbits and wallabies from eating plants
Title Bandicoot, Possum and Quoll gone
Few pointers i want to hit are:
Guaranteed to prevent animals from eating your plants for up to one month
Rain Fast
All natural
Having trouble with rabbits and wallabies eating your garden look no further
needs to sound like i provide the service of spraying
the product for the customers
Book before August 15 and receive $10 off
Contact Brent at Fern Hollow Yard Crew
04xxxxxxxx
My business card is also attached if it could match it
UPDATE: Change in title to Bandicoot, Possum and Quoll gone

```html
<!DOCTYPE html>
<html lang="en">
<head>
<meta charset="utf-8">
<title>Fern Hollow Yard Crew – Bandicoot, Possum and Quoll Deterrent Flyer</title>
<link rel="stylesheet" href="https://fonts.googleapis.com/css2?family=Roboto+Condensed:wght@700&family=Lato:wght@400;700;900&display=swap">
<style>
  :root {
    --lime: #8cc63f;
    --lime-bright: #a6e22e;
    --royal: #1d4fa8;
    --royal-deep: #0f3a8c;
    --charcoal: #2a2a2a;
    --ink: #111111;
    --panel-top: #ffffff;
    --panel-bottom: #e4e4e4;
    --brand-green: #7dbb2a;
    --contact-blue: #2f7de1;
    --white: #ffffff;
  }
  * { margin: 0; padding: 0; box-sizing: border-box; }
  html, body { width: 900px; height: 1200px; overflow: hidden; background: #ffffff; }
  .flyer { position: relative; width: 900px; height: 1200px; overflow: hidden; background: var(--lime); }
  .flyer-shapes { position: absolute; inset: 0; }

  .offer-lead {
    position: absolute; left: 54px; top: 636px;
    font-family: "Roboto Condensed", "Arial Narrow", sans-serif; font-weight: 700;
    text-transform: uppercase; line-height: 1;
  }
  .offer-lead .line { display: block; color: var(--ink); font-size: 52px; letter-spacing: 4.5px; }
  .offer-lead .date { color: var(--royal); font-size: 74px; letter-spacing: 2px; margin: 4px 0 4px; }

  .discount {
    position: absolute; left: 104px; top: 876px; width: 200px;
    font-family: "Roboto Condensed", "Arial Narrow", sans-serif; font-weight: 700;
    color: var(--white); text-align: center; line-height: 0.9;
  }
  .discount .amount { display: block; font-size: 100px; letter-spacing: -2px; }
  .discount .off { display: block; font-size: 46px; margin-left: 60px; margin-top: -12px; }

  .product-panel { position: absolute; left: 466px; top: 596px; width: 434px; padding: 0 26px; }
  .brand {
    font-family: "Lato", sans-serif; font-weight: 700; font-size: 30px;
    color: var(--brand-green); text-align: center; line-height: 1.1; margin-bottom: 26px;
  }
  .headline {
    font-family: "Roboto Condensed", "Arial Narrow", sans-serif; font-weight: 700;
    text-transform: uppercase; line-height: 1.08; font-size: 50px;
  }
  .headline .accent { display: block; color: var(--royal); }
  .headline .rest { display: block; color: var(--charcoal); }
  .guarantee {
    font-family: "Lato", sans-serif; font-weight: 700; font-size: 18px;
    color: var(--ink); line-height: 1.3; margin-top: 16px;
  }

  .features {
    position: absolute; left: 472px; top: 996px; list-style: none; display: flex; gap: 30px;
    font-family: "Lato", sans-serif; font-weight: 700; font-size: 32px; color: var(--ink);
  }
  .features li { display: flex; align-items: center; gap: 8px; }
  .features li::before {
    content: ""; width: 20px; height: 20px; border-radius: 50%; background: var(--lime-bright);
  }

  .contact {
    position: absolute; left: 0; right: 0; top: 1141px; text-align: center;
    font-family: "Lato", sans-serif; font-weight: 900; font-size: 25px; color: var(--white);
  }
  .contact .contact-name { color: var(--contact-blue); }
</style>
</head>
<body>
<main class="flyer">
  <svg class="flyer-shapes" width="900" height="1200" viewBox="0 0 900 1200">
    <defs>
      <linearGradient id="garden-tones" x1="0" y1="0" x2="1" y2="1">
        <stop offset="0" stop-color="#6f8fa8"/>
        <stop offset="0.3" stop-color="#3f7a2a"/>
        <stop offset="0.65" stop-color="#5da32c"/>
        <stop offset="1" stop-color="#7fc23a"/>
      </linearGradient>
      <linearGradient id="panel-fill" x1="0" y1="0" x2="0" y2="1">
        <stop offset="0" stop-color="var(--panel-top)"/>
        <stop offset="1" stop-color="var(--panel-bottom)"/>
      </linearGradient>
      <radialGradient id="badge-fill" cx="0.45" cy="0.4" r="0.7">
        <stop offset="0" stop-color="#2b6fd6"/>
        <stop offset="1" stop-color="var(--royal-deep)"/>
      </radialGradient>
      <polygon id="starburst" points="140,0 115.8,23 129.4,53.6 98.1,65.6 99,99 65.6,98.1 53.6,129.4 23,115.8 0,140 -23,115.8 -53.6,129.4 -65.6,98.1 -99,99 -98.1,65.6 -129.4,53.6 -115.8,23 -140,0 -115.8,-23 -129.4,-53.6 -98.1,-65.6 -99,-99 -65.6,-98.1 -53.6,-129.4 -23,-115.8 0,-140 23,-115.8 53.6,-129.4 65.6,-98.1 99,-99 98.1,-65.6 129.4,-53.6 115.8,-23"/>
    </defs>

    <path class="info-panel" d="M466 380 H900 V960 H482 Q466 960 466 944 Z" fill="url(#panel-fill)"/>

    <path class="header-wave" d="M0 550 C220 540 520 470 900 395 V428 C640 470 330 560 0 616 Z" fill="var(--charcoal)"/>

    <path class="hero-photo" role="img" aria-label="Photo of a tidy front garden with a white porch, hanging flower basket, clipped shrubs, pink flower beds and a white garden arbour on a lawn"
          d="M0 0 H900 V395 C520 460 240 545 0 568 Z" fill="url(#garden-tones)"/>

    <path class="footer-white" d="M0 1100 C260 1040 600 1040 900 1082 V1200 H0 Z" fill="var(--white)"/>
    <path class="footer-blue" d="M0 1116 C260 1062 600 1058 900 1100 V1120 C600 1078 260 1084 0 1140 Z" fill="var(--royal)"/>
    <path class="footer-bar" d="M0 1130 C260 1082 600 1080 900 1118 V1200 H0 Z" fill="var(--charcoal)"/>

    <g class="discount-badge" transform="translate(204 960) scale(0.92)">
      <use href="#starburst" fill="#5a9e22"/>
      <use href="#starburst" fill="url(#badge-fill)" transform="scale(0.88)"/>
    </g>
  </svg>

  <div class="offer-lead">
    <span class="line">Book before</span>
    <span class="line date">August 15</span>
    <span class="line">and receive</span>
  </div>

  <div class="discount">
    <span class="amount">$10</span>
    <span class="off">OFF</span>
  </div>

  <section class="product-panel">
    <p class="brand">Fern Hollow Yard Crew</p>
    <h1 class="headline">
      <span class="accent">Keep Bandicoot,</span>
      <span class="rest">Possum and</span>
      <span class="rest">Quoll gone</span>
    </h1>
    <p class="guarantee">Pests eating your garden? Look no further – we spray it for you. Guaranteed to stop animals eating your plants for up to one month</p>
  </section>

  <ul class="features">
    <li>Rain Fast</li>
    <li>All natural</li>
  </ul>

  <p class="contact">Contact <span class="contact-name">Brent Today</span> 04XXXXXXXX</p>
</main>
</body>
</html>
```